home theater/ flat panel TV installation/ computer networking

single page flyer front and back, I am paying for adress labels so it should be 8 1/2" x 11" tri-fold with a place for the labels to go and be easy to mail.

Brightline Media

Charlotte NC 28917

http://www.brightlinemedianc.example/

call today for your no cost consultation  704-418-2263

Call today for your no cost consultation!    704-418-2263  Brightline Media

If your new home came with a finished basement, or you are

finishing it yourself, consider making part of it into a great home

theater. Why not add a fantastic High Definition projector and 100”

screen to your lovely new home? Experience satellite and cable TV,

video games, and of course, movies like you have never seen or

heard before. The cost of the system is probably a lot less than you

think. Finally, we install everything and provide a single programmed

remote to operate the entire system, easily! Already have a High

Definition TV? Let us integrate it with speakers, programmable

remotes, even a popcorn machine! Free consultations at your

request.

professional home theater designer and network cable installations in Texas

regular size.  I am picturing 8 1/2" x 11"  tri-fold.   I have never had a flyer before and am willing to accept different sizes.   

 

Target Market(s)

These will be sent to new home owners already looking for these services. I am a small company trying to say "we are the best".

These are the services we sell... (feel free to High-light or bullet)

-Home Theater
-High Definition TV
-Surround Sound
-All-in-One remotes
-Computer Networks
-Liscenced Electrician
-Lighting control

Industry/Entity Type

Computer

Requirements
Must have
• most of these photos. I am willing to pay for something better if available.  maybe a family or something.

• customer testimonial (should be italisized)

• "Brightline Media showed up on time, cleaned up after themselves, they we great!"

• "...we left the key under the mat, when we got home the TV was on the wall..."
Nice to have
• sonic wave from business card.eps file
• a few more photos

```html
<!DOCTYPE html>
<html lang="en">
<head>
<meta charset="utf-8">
<title>Brightline Media – Tri-fold Mailer</title>
<link rel="stylesheet" href="https://fonts.googleapis.com/css2?family=Exo+2:wght@400;600;700&family=Hind:wght@400;600&family=Crimson+Text:ital,wght@0,600;1,400&display=swap">
<style>
  :root{
    --page:#ffffff;
    --sheet-top:#e9f2f8;
    --sheet-bottom:#d3e4f0;
    --steel:#5d8fae;
    --steel-dark:#4a7896;
    --brand:#2f7fc4;
    --ink:#4f565c;
    --ink-soft:#6b7379;
    --white:#ffffff;
    --photo-dark:#2c2e31;
    --photo-mid:#8a8d90;
  }
  *{box-sizing:border-box;margin:0;padding:0}
  html,body{width:1200px;height:532px;overflow:hidden;background:var(--page)}
  body{position:relative;font-family:"Hind",sans-serif;color:var(--ink)}
  .sheet{
    position:absolute;top:110px;width:400px;height:311px;overflow:hidden;
    background:linear-gradient(160deg,var(--sheet-top),var(--sheet-bottom));
    box-shadow:0 3px 8px rgba(0,0,0,.35);
  }
  .sheet--outside{left:180px}
  .sheet--inside{left:620px}
  .abs{position:absolute}
  .photo{position:absolute;display:block}
  .brand-name{font-family:"Hind",sans-serif;font-weight:600;color:var(--brand);white-space:nowrap;letter-spacing:.2px}
  .brand-tagline{font-size:4.5px;color:var(--ink-soft);letter-spacing:.3px}

  /* outside panel */
  .cover-photo{left:0;top:0;width:134px;height:311px;background:linear-gradient(180deg,var(--photo-dark),#55585b 50%,var(--photo-dark))}
  .stamp-box{left:234px;top:11px;width:24px;height:29px;background:var(--white)}
  .label-box{left:149px;top:156px;width:104px;height:66px;background:var(--white)}
  .cover-brand{right:22px;top:95px;text-align:left}
  .cover-brand .brand-name{font-size:15px;line-height:1}
  .mail-block{left:134px;width:174px;top:236px;text-align:center}
  .mail-block .brand-name{font-size:10px;line-height:1}
  .mail-block .city{font-size:5.5px;margin-top:7px}
  .mail-block .web{font-size:4.5px;margin-top:1px}
  .mail-block .call{font-size:6px;margin-top:3px}
  .mail-block .phone{font-family:"Exo 2",sans-serif;font-weight:600;font-size:10px;margin-top:2px;color:var(--ink)}

  /* inside panel */
  .headline{left:16px;top:14px;font-family:"Exo 2",sans-serif;font-weight:600;font-size:7.5px;letter-spacing:.8px;color:var(--steel)}
  .headline-rule{left:16px;top:29px;width:105px;height:1px;background:var(--steel)}
  .body-copy{font-size:5.6px;line-height:1.55;text-align:center;color:var(--ink)}
  .intro{left:12px;top:44px;width:120px}
  .band{background:var(--steel);color:var(--white);font-family:"Exo 2",sans-serif;font-weight:600;text-align:center;text-transform:uppercase;display:flex;align-items:center;justify-content:center}
  .band--projector{left:0;top:87px;width:135px;height:40px;font-size:5.3px;line-height:1.7;padding:0 8px}
  .band--hdtv{left:271px;top:142px;width:135px;height:25px;font-size:5px}
  .offer{left:12px;top:137px;width:120px}
  .remotes{left:26px;top:222px;width:75px;height:73px;background:linear-gradient(90deg,#b9cde0,#3a3d41 60%,#26282b)}
  .services{left:149px;top:28px;width:104px;height:120px;background:var(--steel);color:var(--white);padding:12px 0 0 11px}
  .services h2{font-family:"Exo 2",sans-serif;font-weight:600;font-size:7px;letter-spacing:.6px;margin-bottom:5px}
  .services li{list-style:none;font-size:5.6px;line-height:2.15}
  .services li::before{content:"• "}
  .photo--living{left:308px;top:0;width:98px;height:69px;background:linear-gradient(160deg,#d8c79a,#8c6b47)}
  .photo--tvwall{left:254px;top:71px;width:51px;height:64px;background:linear-gradient(160deg,#5b3a2a,#2c211c)}
  .photo--lounge{left:308px;top:71px;width:98px;height:64px;background:linear-gradient(160deg,#6b4a3c,#c9b8a5)}
  .photo--theater{left:149px;top:151px;width:104px;height:85px;background:linear-gradient(180deg,#6d4a2e,#3a2518 70%,#1e1612)}
  .integrate{left:288px;top:177px;width:100px}
  .testimonial{left:149px;top:240px;width:110px;font-family:"Crimson Text",serif}
  .testimonial h3{font-weight:600;font-size:6.2px;margin-bottom:4px;color:var(--ink)}
  .testimonial blockquote{font-style:italic;font-size:5.3px;line-height:1.35;margin-bottom:5px;color:var(--ink)}
  .consult{left:271px;top:216px;width:127px;height:86px;border:1px solid var(--ink-soft);padding:8px 9px;font-family:"Exo 2",sans-serif;color:var(--ink)}
  .consult h2{font-weight:600;font-size:7px;line-height:1.25;letter-spacing:.4px;text-transform:uppercase}
  .consult .web{font-family:"Hind",sans-serif;font-size:5.6px;margin-top:7px}
  .consult .call{font-size:6.2px;line-height:1.45;margin-top:7px}
  .consult .call strong{font-weight:700;font-size:7.2px}
</style>
</head>
<body>

<section class="sheet sheet--outside" aria-label="Mailer outside panels">
  <div class="photo cover-photo" role="img" aria-label="Black and white photo of a wall of flat panel televisions"></div>
  <div class="abs stamp-box" aria-label="Postage area"></div>
  <div class="abs cover-brand">
    <div class="brand-name">Brightline Media</div>
    <div class="brand-tagline">Audio · Video · Structured Wiring</div>
  </div>
  <div class="abs label-box" aria-label="Address label area"></div>
  <div class="abs mail-block">
    <div class="brand-name">Brightline Media</div>
    <div class="brand-tagline">Audio · Video · Structured Wiring</div>
    <p class="city">Charlotte NC 28917</p>
    <p class="web">www.brightlinemedianc.example</p>
    <p class="call">Call today for your no cost consultation</p>
    <p class="phone">704-418-2263</p>
  </div>
</section>

<section class="sheet sheet--inside" aria-label="Mailer inside panels">
  <h1 class="abs headline">EXPERIENCE, PROFESSIONAL AND RELIABLE.</h1>
  <div class="abs headline-rule"></div>
  <p class="abs body-copy intro">If your new home came with a finished basement, or you are finishing it yourself, consider making part of it into a great home theater.</p>
  <div class="abs band band--projector">Why not add a fantastic High Definition projector and 100" screen to your lovely new home?</div>
  <p class="abs body-copy offer">Experience satellite and cable TV, video games, and of course, movies like you have never seen or heard before. The cost of the system is probably a lot less than you think. Finally, we install everything and provide a single programmed remote to operate the entire system, easily!</p>
  <div class="photo remotes" role="img" aria-label="Three programmable universal remote controls"></div>

  <div class="abs services">
    <h2>SERVICES WE SELL</h2>
    <ul>
      <li>Home Theater</li>
      <li>High Definition TV</li>
      <li>Surround Sound</li>
      <li>All-in-One remotes</li>
      <li>Computer Networks</li>
      <li>Liscenced Electrician</li>
      <li>Lighting control</li>
    </ul>
  </div>
  <div class="photo photo--living" role="img" aria-label="Living room with a TV mounted above a brick fireplace"></div>
  <div class="photo photo--tvwall" role="img" aria-label="Wood-paneled media wall with a flat screen"></div>
  <div class="photo photo--lounge" role="img" aria-label="Basement lounge with curtained screen and armchairs"></div>
  <div class="photo photo--theater" role="img" aria-label="Dedicated home theater room with leather recliners"></div>

  <div class="abs band band--hdtv">Already have a High Definition TV?</div>
  <p class="abs body-copy integrate">Let us integrate it with speakers, programmable remotes, even a popcorn machine!</p>

  <div class="abs testimonial">
    <h3>Customer Testimonial</h3>
    <blockquote>"Brightline Media showed up on time, cleaned up after themselves, they we great!"</blockquote>
    <blockquote>"...we left the key under the mat, when we got home the TV was on the wall..."</blockquote>
  </div>

  <div class="abs consult">
    <h2>Free consultations<br>at your request.</h2>
    <p class="web">www.brightlinemedianc.example</p>
    <p class="call">Call today for your no cost consultation at <strong>704-418-2263</strong></p>
  </div>
</section>

</body>
</html>
```